Interior Design/ decoration business card design

This card is for my Interior Design and Decoration business and later I will also be selling homewares. I would like the card to be very simple in design and like either white, duck egg blue , aquas or metallics on a flat mat card excellent quality card. It needs to be well designed as that is my field. I dont like fuss, the simpler the better. I would like a styalised wren under the name wren if possible. SIMPLE, STYLISH, CLASSIC, TASTEFUL

Target Market(s)

40 + year olds who are building or rennovating.

Industry/Entity Type

Business

Contact Information for Business Card

Wren
styling, design, homeware

Maren Tulloch
p 0437165093
e maren@wrenliving.com.au
w wrenliving.com.au

Requirements
Must have
• very simple, stylish, classic, sophisticated. Simple and easy to read text that is a print similar to attached image. I like simple round A's though not as in attached image.

Double sided. It wont save as double sided for some reason!!
Should not have
• not too much colour, No animated / cartoon pictures.

```html
<!DOCTYPE html>
<html lang="en">
<head>
<meta charset="utf-8">
<title>Wren business card – front and back</title>
<link href="https://fonts.googleapis.com/css2?family=Questrial&display=swap" rel="stylesheet">
<style>
  :root {
    --backdrop: #efeae0;
    --duck-egg: #bcd9d8;
    --duck-egg-light: #dcf3f1;
    --ink: #4a3c36;
  }
  html, body {
    margin: 0;
    padding: 0;
    width: 1200px;
    height: 1000px;
    overflow: hidden;
    background: var(--backdrop);
  }
  .canvas {
    position: relative;
    width: 1200px;
    height: 1000px;
    font-family: "Questrial", "Helvetica Neue", Arial, sans-serif;
    color: var(--ink);
  }
  .card {
    position: absolute;
    width: 750px;
    height: 462px;
    background: var(--duck-egg);
    overflow: hidden;
  }
  .card--front {
    left: 50px;
    top: 35px;
    background: radial-gradient(circle at 42% 40%, var(--duck-egg-light) 0%, #cfe9e7 35%, var(--duck-egg) 80%);
  }
  .card--back {
    left: 387px;
    top: 514px;
  }
  .holder-name {
    position: absolute;
    right: 68px;
    top: 88px;
    margin: 0;
    font-size: 64px;
    font-weight: 400;
    line-height: 1;
    letter-spacing: 0.5px;
  }
  .contact {
    position: absolute;
    right: 68px;
    top: 176px;
    margin: 0;
    padding: 0;
    list-style: none;
    text-align: right;
    font-size: 24px;
    line-height: 30.5px;
  }
  .contact__phone {
    letter-spacing: 2px;
  }
  .brand {
    position: absolute;
    left: 0;
    right: 0;
    top: 128px;
    margin: 0;
    text-align: center;
    font-size: 76px;
    font-weight: 400;
    line-height: 1;
    letter-spacing: 1px;
  }
  .services {
    position: absolute;
    left: 0;
    right: 0;
    top: 282px;
    margin: 0;
    text-align: center;
    font-size: 22px;
    line-height: 1;
  }
  .services__item + .services__item {
    border-left: 2px solid var(--ink);
    margin-left: 4px;
    padding-left: 5px;
  }
</style>
</head>
<body>
<main class="canvas">
  <section class="card card--front" aria-label="Card front">
    <h1 class="holder-name">Maren Tulloch</h1>
    <ul class="contact">
      <li class="contact__phone">0437165093</li>
      <li class="contact__email">maren@wrenliving.com.au</li>
      <li class="contact__web">www.wrenliving.com.au</li>
    </ul>
  </section>

  <section class="card card--back" aria-label="Card back">
    <p class="brand">wren</p>
    <p class="services"><span class="services__item">decoration</span><span class="services__item">styling</span><span class="services__item">homeware</span></p>
  </section>
</main>
</body>
</html>
```